IT’S NOT A CLEANING, IT’S YOUR LIFE! TOP TEN REASONS WHY THIS IS NOT JUST A “CLEANING”

We made a list for our patients to let them know why our hygiene appointments are different than other cleanings. Since this is a lot of information, we would like it easily readable within 4-5 feet but we do not want the post to be HUGE. Please see below:

IT’S NOT A CLEANING, IT’S YOUR LIFE!
TOP TEN REASONS WHY THIS IS NOT JUST A “CLEANING”

10. We make you look better. Healthy teeth and gums are more attractive. Recent studies
show that the smile is the first thing people notice and that people with better looking teeth
are more confident and successful.

9. We can relieve your headaches. During your hygiene visit we evaluate for serious bite
issues, many of which lead to muscle soreness, headaches, and migraines.

8. We check for oral cancer. Oral cancer kills 1 person per hour 24 hours a day. The death rate for oral cancer is higher than cancers we routinely hear about such as cervical, thyroid and skin cancer.

7. We make you smell better. During your hygiene visit we eliminate many of the germs that live under your gum tissue and cause bad breath.

6. We save you money. By utilizing the latest dental technology (digital x-rays, mouth
cameras, and magnification glasses) we can help with early detection of tooth and gum
problems and save you the cost of gum surgery, root canals, and implants.

5. We clean in places you cannot. We clean under the gum line and between teeth where
most of the germs hide and cause dental disease. 40% of the bacteria in your mouth lives in
between your teeth.

4. We prevent pain. We identify tooth decay that can lead to nerve involvement and pain,
root canal, and tooth loss.

3. We save your teeth. Most tooth loss is from periodontal/gum disease. At each visit we
evaluate the health of your gums and bone with our periodontal screening. Periodontal
disease, like high blood pressure, is symptomless until it is in advanced stages.

2. We protect your loved ones. Studies have proven that the bacteria that cause dental
disease can be transmitted from person to person. Think about that the next time you kiss
someone!

1. We prolong life. Researchers have linked the inflammation and infection found in the
mouth to heart attacks, strokes, and Alzheimer’s. By reducing infection in your mouth we can
greatly improve your overall health!

```html
<!DOCTYPE html>
<html lang="en">
<head>
<meta charset="utf-8">
<title>It's Not Just a Cleaning. It's Your Life!</title>
<link href="https://fonts.googleapis.com/css2?family=Oswald:wght@300;500;600&family=Playfair+Display:wght@700;900&family=Montserrat:wght@300;400;800&display=swap" rel="stylesheet">
<style>
  :root {
    --navy: #2d2e6e;
    --sky: #62aedf;
    --cream: #f7ede2;
    --ice: #cfe4f5;
    --ink: #111111;
    --band: #ececec;
    --pulse: #555555;
    --paper: #ffffff;
    --tooth-light: #fafafa;
    --tooth-shade: #d6d6d6;
  }
  * { box-sizing: border-box; margin: 0; padding: 0; }
  html, body { width: 900px; height: 1200px; overflow: hidden; background: var(--paper); }
  .poster { position: relative; width: 900px; height: 1200px; font-family: 'Montserrat', sans-serif; color: var(--ink); }

  .teeth { position: absolute; left: 275px; width: 350px; background: linear-gradient(180deg, var(--tooth-light), var(--tooth-shade)); }
  .teeth--upper { top: 18px; height: 72px; border-radius: 50% 50% 40% 40% / 30% 30% 70% 70%; }
  .teeth--lower { top: 178px; height: 66px; border-radius: 40% 40% 50% 50% / 70% 70% 30% 30%; }

  .masthead { position: absolute; top: 94px; left: 0; width: 900px; text-align: center; }
  .masthead__kicker { font-weight: 400; font-size: 17px; letter-spacing: 2.5px; }
  .masthead__title { display: inline-block; margin-top: 2px; font-family: 'Playfair Display', serif; font-weight: 900; font-size: 46px; line-height: 1.05; padding: 0 4px 4px; border-bottom: 1.5px solid var(--ink); }
  .masthead__title span { text-decoration: underline; text-decoration-thickness: 2px; text-underline-offset: 6px; }

  .subhead { position: absolute; top: 266px; left: 80px; width: 740px; font-family: 'Oswald', sans-serif; font-weight: 300; font-size: 27px; letter-spacing: 0.3px; white-space: nowrap; }
  .subhead strong { font-family: 'Montserrat', sans-serif; font-weight: 800; font-size: 25px; letter-spacing: 0.5px; }

  .reason { position: absolute; width: 230px; height: 230px; padding: 12px 10px 0 10px; overflow: hidden; }
  .reason--navy { background: var(--navy); color: var(--ice); }
  .reason--sky { background: var(--sky); color: var(--navy); }
  .reason--cream { background: var(--cream); color: var(--navy); }
  .reason__number { text-align: center; font-family: 'Playfair Display', serif; font-weight: 900; font-size: 44px; line-height: 1; }
  .reason--sky .reason__number { color: var(--paper); }
  .reason__heading { margin-top: 8px; font-family: 'Oswald', sans-serif; font-weight: 600; font-size: 15px; line-height: 22px; letter-spacing: -0.3px; text-transform: uppercase; white-space: nowrap; }
  .reason--sky .reason__heading { color: var(--paper); }
  .reason__body { position: relative; z-index: 1; margin-top: 10px; font-weight: 400; font-size: 10px; line-height: 1.22; }
  .reason--navy .reason__body { font-weight: 300; }
  .wrap-gap { float: right; }

  .icon { position: absolute; }
  .icon-placeholder { position: absolute; border-radius: 10px; }

  .reason--10 { left: 80px; top: 328px; }
  .reason--9 { left: 335px; top: 328px; }
  .reason--8 { left: 590px; top: 328px; }
  .reason--7 { left: 80px; top: 583px; }
  .reason--6 { left: 335px; top: 583px; }
  .reason--5 { left: 590px; top: 583px; }
  .reason--4 { left: 80px; top: 838px; }
  .reason--3 { left: 335px; top: 838px; }
  .reason--2 { left: 590px; top: 838px; }

  .closing { position: absolute; left: 80px; top: 1093px; width: 740px; height: 82px; background: var(--band); }
  .closing__icon { position: absolute; left: 22px; top: 16px; }
  .closing__title { position: absolute; left: 94px; top: 22px; font-family: 'Oswald', sans-serif; font-weight: 500; font-size: 33px; line-height: 1; color: var(--pulse); white-space: nowrap; }
  .closing__title b { font-family: 'Playfair Display', serif; font-weight: 900; margin-right: 8px; }
  .closing__body { position: absolute; left: 366px; top: 20px; width: 366px; font-size: 10px; line-height: 1.3; color: var(--pulse); }
</style>
</head>
<body>
<main class="poster">
  <div class="teeth teeth--upper" role="img" aria-label="Upper row of white teeth"></div>
  <div class="teeth teeth--lower" role="img" aria-label="Lower row of white teeth"></div>

  <header class="masthead">
    <p class="masthead__kicker">IT’S NOT JUST A CLEANING.</p>
    <h1 class="masthead__title">It’s <span>your</span> life!</h1>
  </header>

  <h2 class="subhead">TOP TEN REASONS WHY THIS IS <strong>MORE THAN ‘JUST A CLEANING.’</strong></h2>

  <section class="reason reason--navy reason--10">
    <div class="reason__number">10</div>
    <h3 class="reason__heading">We make you look better.</h3>
    <p class="reason__body"><span class="wrap-gap" style="width:100px;height:134px;shape-outside:inset(25px 0 0 0)"></span>Healthy teeth and gums are more attractive. Recent studies show that the smile is the first thing people notice and that people with better looking teeth are more confident and successful.</p>
    <svg class="icon" style="left:118px;top:148px" width="102" height="62" viewBox="0 0 102 62">
      <path d="M2 30 C18 8 34 2 44 8 C48 10 50 12 51 12 C52 12 54 10 58 8 C68 2 84 8 100 30 C84 56 68 60 51 60 C34 60 18 56 2 30 Z" fill="var(--ice)"/>
      <path d="M10 30 C30 26 40 34 51 30 C62 34 72 26 92 30 C72 38 62 36 51 36 C40 36 30 38 10 30 Z" fill="var(--navy)"/>
    </svg>
  </section>

  <section class="reason reason--sky reason--9">
    <div class="reason__number">9</div>
    <h3 class="reason__heading">We can relieve your headaches.</h3>
    <p class="reason__body"><span class="wrap-gap" style="width:106px;height:134px"></span>During your hygiene visit we evaluate for serious bite issues, many of which lead to muscle soreness, headaches, and migraines.</p>
    <div class="icon-placeholder" style="left:124px;top:118px;width:90px;height:90px;background:var(--paper);opacity:.85" role="img" aria-label="Patient reclining in a dental chair under a lamp"></div>
  </section>

  <section class="reason reason--cream reason--8">
    <div class="reason__number">8</div>
    <h3 class="reason__heading">We check for oral cancer.</h3>
    <p class="reason__body"><span class="wrap-gap" style="width:92px;height:134px"></span>Oral cancer kills 1 person per hour 24 hours a day. The death rate for oral cancer is higher than cancers we routinely hear about such as cervical, thyroid and skin cancer.</p>
    <svg class="icon" style="left:124px;top:118px" width="92" height="94" viewBox="0 0 92 94">
      <circle cx="52" cy="40" r="30" fill="none" stroke="var(--navy)" stroke-width="9"/>
      <line x1="30" y1="62" x2="8" y2="86" stroke="var(--navy)" stroke-width="12" stroke-linecap="round"/>
      <path d="M40 28 C44 24 48 26 52 28 C56 26 60 24 64 28 C67 32 65 40 62 46 C61 52 60 56 58 56 C56 56 55 48 52 46 C49 48 48 56 46 56 C44 56 43 52 42 46 C39 40 37 32 40 28 Z" fill="none" stroke="var(--navy)" stroke-width="2.5"/>
    </svg>
  </section>

  <section class="reason reason--cream reason--7">
    <div class="reason__number">7</div>
    <h3 class="reason__heading">We make you smell better.</h3>
    <p class="reason__body">During your hygiene visit we eliminate many of the germs that live under your gum tissue and cause bad breath.</p>
    <svg class="icon" style="left:72px;top:136px" width="84" height="84" viewBox="0 0 84 84">
      <g stroke="var(--navy)" stroke-width="3" stroke-linecap="round">
        <line x1="42" y1="42" x2="42" y2="6"/><line x1="42" y1="42" x2="42" y2="78"/>
        <line x1="42" y1="42" x2="6" y2="42"/><line x1="42" y1="42" x2="78" y2="42"/>
        <line x1="42" y1="42" x2="16" y2="16"/><line x1="42" y1="42" x2="68" y2="68"/>
        <line x1="42" y1="42" x2="68" y2="16"/><line x1="42" y1="42" x2="16" y2="68"/>
      </g>
      <g fill="var(--navy)">
        <circle cx="42" cy="6" r="4.5"/><circle cx="42" cy="78" r="4.5"/><circle cx="6" cy="42" r="4.5"/><circle cx="78" cy="42" r="4.5"/>
        <circle cx="16" cy="16" r="4.5"/><circle cx="68" cy="68" r="4.5"/><circle cx="68" cy="16" r="4.5"/><circle cx="16" cy="68" r="4.5"/>
        <circle cx="42" cy="42" r="22"/>
      </g>
      <g fill="var(--cream)"><circle cx="34" cy="36" r="4"/><circle cx="48" cy="48" r="3"/><circle cx="50" cy="32" r="2.5"/></g>
    </svg>
  </section>

  <section class="reason reason--navy reason--6">
    <div class="reason__number">6</div>
    <h3 class="reason__heading">We save you money.</h3>
    <p class="reason__body"><span class="wrap-gap" style="width:90px;height:134px;shape-outside:inset(37px 0 0 0)"></span>By utilizing the latest dental technology (digital x-rays, mouth cameras, and magnification glasses) we can help with early detection of tooth and gum problems and save you the cost of gum surgery, root canals, and implants.</p>
    <svg class="icon" style="left:142px;top:146px" width="68" height="66" viewBox="0 0 68 66">
      <g fill="var(--navy)" stroke="var(--ice)" stroke-width="3">
        <ellipse cx="34" cy="56" rx="28" ry="7"/>
        <ellipse cx="34" cy="48" rx="28" ry="7"/>
        <ellipse cx="34" cy="40" rx="28" ry="7"/>
        <circle cx="34" cy="20" r="17"/>
      </g>
      <text x="34" y="27" text-anchor="middle" font-family="Montserrat, sans-serif" font-weight="800" font-size="20" fill="var(--ice)">$</text>
    </svg>
  </section>

  <section class="reason reason--sky reason--5">
    <div class="reason__number">5</div>
    <h3 class="reason__heading">We clean in places you cannot.</h3>
    <p class="reason__body"><span class="wrap-gap" style="width:80px;height:134px"></span>We clean under the gum line and between teeth where most of the germs hide and cause dental disease. 40% of the bacteria in your mouth lives in between your teeth.</p>
    <svg class="icon" style="left:150px;top:120px" width="64" height="96" viewBox="0 0 64 96">
      <g fill="none" stroke="var(--paper)" stroke-width="4" stroke-linecap="round">
        <circle cx="16" cy="16" r="12"/>
        <line x1="16" y1="28" x2="16" y2="92"/>
        <path d="M58 4 C56 12 48 18 44 22 L44 92"/>
      </g>
      <circle cx="16" cy="16" r="6" fill="var(--paper)"/>
    </svg>
  </section>

  <section class="reason reason--sky reason--4">
    <div class="reason__number">4</div>
    <h3 class="reason__heading">We prevent pain.</h3>
    <p class="reason__body">We identify tooth decay that can lead to nerve involvement and pain, root canal, and tooth loss.</p>
    <svg class="icon" style="left:80px;top:144px" width="56" height="70" viewBox="0 0 56 70">
      <path d="M8 8 C16 0 24 4 28 6 C32 4 40 0 48 8 C56 18 50 32 46 42 C44 54 42 66 38 66 C34 66 33 50 28 46 C23 50 22 66 18 66 C14 66 12 54 10 42 C6 32 0 18 8 8 Z" fill="none" stroke="var(--paper)" stroke-width="4" stroke-linejoin="round"/>
      <g fill="var(--paper)"><circle cx="20" cy="18" r="3"/><circle cx="34" cy="24" r="3.5"/><circle cx="24" cy="32" r="2.5"/><circle cx="38" cy="14" r="2"/></g>
    </svg>
  </section>

  <section class="reason reason--cream reason--3">
    <div class="reason__number">3</div>
    <h3 class="reason__heading">We save your teeth.</h3>
    <p class="reason__body"><span class="wrap-gap" style="width:92px;height:134px;shape-outside:inset(37px 0 0 0)"></span>Most tooth loss is from periodontal/ gum disease. At each visit we evaluate the health of your gums and bone with our periodontal screening. Periodontal disease, like high blood pressure, is symptomless until it is in advanced stages.</p>
    <svg class="icon" style="left:136px;top:150px" width="84" height="64" viewBox="0 0 84 64">
      <rect x="28" y="2" width="28" height="14" rx="4" fill="none" stroke="var(--navy)" stroke-width="5"/>
      <rect x="2" y="14" width="80" height="48" rx="6" fill="var(--navy)"/>
      <rect x="14" y="14" width="4" height="48" fill="var(--cream)"/>
      <rect x="66" y="14" width="4" height="48" fill="var(--cream)"/>
      <circle cx="42" cy="38" r="14" fill="var(--cream)"/>
      <path d="M38 28 h8 v6 h6 v8 h-6 v6 h-8 v-6 h-6 v-8 h6 Z" fill="var(--navy)"/>
    </svg>
  </section>

  <section class="reason reason--navy reason--2">
    <div class="reason__number">2</div>
    <h3 class="reason__heading">We protect your loved ones.</h3>
    <p class="reason__body"><span class="wrap-gap" style="width:80px;height:134px"></span>Studies have proven that the bacteria that cause dental disease can be transmitted from person to person. Think about that the next time you kiss someone!</p>
    <div class="icon-placeholder" style="left:142px;top:112px;width:72px;height:100px;background:var(--ice);opacity:.8" role="img" aria-label="Silhouette of an adult holding a child's hand"></div>
  </section>

  <footer class="closing">
    <svg class="closing__icon" width="52" height="52" viewBox="0 0 52 52">
      <circle cx="26" cy="26" r="26" fill="var(--pulse)"/>
      <polyline points="6,28 16,28 20,20 25,38 30,12 34,28 46,28" fill="none" stroke="var(--paper)" stroke-width="3" stroke-linejoin="round" stroke-linecap="round"/>
    </svg>
    <p class="closing__title"><b>1</b>WE PROLONG LIFE.</p>
    <p class="closing__body">Researchers have linked the inflammation and infection found in the mouth to heart attacks, strokes, and Alzheimer’s. By reducing infection in your mouth we can greatly improve your overall health!</p>
  </footer>
</main>
</body>
</html>
```